Simple Business Cards for Self-employed Coach

Simple business card with a design that includes the QLT logo.
Using either only the logo color or additional colors that match the logo.

Meridian Guides reach deeply into the past, gathering wisdom from East and West, while still staying current with the frontiers of new discovery in cognitive science, genetics, and other disciplines. see https://www.brightharborpath.example/what-is-integral-coaching/

Target Market(s)

Coaching Clients in Tokyo /Asia; in business organizations, but also outside

Industry/Entity Type

Life Coaching

Contact Information for Business Card

Lukas Brenning
Certified Meridian Guide

3-2-48 Kamiyoshi
Nakarino 164-0392
Tokyo, Japan

Phone: +81 70 4817 5062
E-Mail: lukas.brenning@mailora.example

Font styles to use
Sans Serif

Colors
00a990

Requirements
Must have
• include uploaded logo
• color fitting with QLT logo color
Nice to have
• simple, elegant design
Should not have
• clutter

```html
<!DOCTYPE html>
<html lang="en">
<head>
<meta charset="utf-8">
<title>Lukas Brenning – Business Card</title>
<link rel="stylesheet" href="https://fonts.googleapis.com/css2?family=Lato:ital,wght@0,400;0,700;1,300&display=swap">
<style>
  :root {
    --teal: #007a6c;
    --ink: #1c1c1c;
    --muted: #4a4a4a;
    --card: #ffffff;
    --backdrop: #ececec;
  }
  html, body {
    margin: 0;
    padding: 0;
    width: 1200px;
    height: 586px;
    overflow: hidden;
    background: var(--backdrop);
    font-family: "Lato", sans-serif;
  }
  .business-card {
    position: absolute;
    left: 150px;
    top: 23px;
    width: 900px;
    height: 540px;
    background: var(--card);
    overflow: hidden;
  }
  .brand {
    position: absolute;
    left: 428px;
    top: 62px;
    transform: translateX(-50%);
    display: flex;
    align-items: center;
    gap: 18px;
  }
  .brand-square {
    width: 56px;
    height: 56px;
    background: var(--teal);
  }
  .brand-name {
    font-weight: 700;
    font-size: 84px;
    line-height: 1;
    letter-spacing: 10px;
    color: var(--teal);
  }
  .contact {
    position: absolute;
    left: 62px;
    top: 355px;
  }
  .contact-line {
    display: flex;
    align-items: center;
    gap: 10px;
    font-size: 22px;
    color: var(--ink);
    height: 37px;
  }
  .contact-line svg {
    width: 24px;
    height: 20px;
    fill: var(--teal);
    flex: none;
  }
  .address {
    margin-top: 10px;
    font-weight: 700;
    font-size: 22px;
    line-height: 31px;
    color: var(--teal);
  }
  .identity {
    position: absolute;
    right: 58px;
    top: 368px;
    text-align: right;
  }
  .person-name {
    font-weight: 700;
    font-size: 34px;
    line-height: 40px;
    color: var(--teal);
  }
  .person-title {
    font-weight: 300;
    font-style: italic;
    font-size: 23px;
    line-height: 32px;
    color: var(--muted);
  }
  .footer-band {
    position: absolute;
    left: 0;
    bottom: 0;
    width: 100%;
    height: 19px;
    background: var(--teal);
  }
</style>
</head>
<body>
  <div class="business-card">
    <div class="brand">
      <div class="brand-square"></div>
      <div class="brand-name">QLT</div>
    </div>

    <div class="contact">
      <div class="contact-line">
        <svg viewBox="0 0 24 20" aria-hidden="true">
          <path d="M2 7c0-3 5-5 10-5s10 2 10 5v2h-5V7c-1-1-3-1.5-5-1.5S8 6 7 7v2H2z"/>
          <path d="M6 10h12l3 8H3z"/>
        </svg>
        <span>+81 70 4817 5062</span>
      </div>
      <div class="contact-line">
        <svg viewBox="0 0 24 20" aria-hidden="true">
          <path d="M2 3h20v14H2z M4 5l8 6 8-6" fill="var(--teal)"/>
          <path d="M4 5l8 6 8-6" fill="none" stroke="#fff" stroke-width="1.6"/>
        </svg>
        <span>lukas.brenning@mailora.example</span>
      </div>
      <div class="address">
        3-2-48 Kamiyoshi<br>
        Nakarino 164-0392, Tokyo, Japan
      </div>
    </div>

    <div class="identity">
      <div class="person-name">Lukas Brenning</div>
      <div class="person-title">Certified Meridian Guide</div>
    </div>

    <div class="footer-band"></div>
  </div>
</body>
</html>
```